Why engage Insight Harborworks?

We are starting a new company that will perform usability consulting and offer usability lab rental. We are in need a one page description flyer.
Updates

Wow! We saw some very interesting and creative flyers posted for review in our contest.

Unfortunately, my schedule became a bit crazy and I may not get back to evaluating them until next week :(  In the meantime, I did want to say thank you for your entries!

Cheers!
Merle

Target Market(s)

product designers, human factors/usability researchers, consumer researcher firms, etc

Industry/Entity Type

It Company

Requirements
Must have
• We would like to see designs with a simple, yet modern, sophisticated feel. I will include our logo images that need to be incorporated along with the font used.

The file called flyer.pdf has all of the information that needs to be included.

Please include 1-3 appropriate stock photos. Please see text in flyer.pdf for description of our services.

Nice to have
• Additionally, there is a sample flyer design that we like for reference. Not a requirement...it is just a reference for the kind of style that we are looking for.

```html
<!DOCTYPE html>
<html lang="en">
<head>
<meta charset="utf-8">
<title>Insight Harborworks – Flyer</title>
<link href="https://fonts.googleapis.com/css2?family=Montserrat:wght@400&family=Libre+Baskerville:ital,wght@1,700&family=Open+Sans:wght@400;700&display=swap" rel="stylesheet">
<style>
  :root{
    --backdrop:#e4e4e4;
    --paper:#ffffff;
    --navy:#1d3a6b;
    --green:#8dc63f;
    --orange:#f37021;
    --text:#4a4a4a;
    --chalk-dark:#2e2f30;
    --chalk-mid:#4a4b4c;
  }
  *{box-sizing:border-box;margin:0;padding:0}
  html,body{width:1200px;height:768px;overflow:hidden;background:var(--backdrop)}
  body{position:relative;font-family:"Open Sans",Arial,sans-serif;color:var(--text)}

  .flyer{position:absolute;left:320px;top:21px;width:560px;height:725px;background:var(--paper);
    box-shadow:0 6px 18px rgba(0,0,0,.18);overflow:hidden}

  .accent-tab{position:absolute;left:28px;top:0;width:82px;height:9px;background:var(--orange);border-radius:0 0 5px 5px}
  .accent-bar{position:absolute;right:40px;bottom:0;width:70px;height:9px;background:var(--orange);border-radius:5px 5px 0 0}

  .main{position:absolute;left:0;top:0;width:336px;height:100%;padding:30px 22px 0 26px}
  .brand{display:flex;align-items:center;gap:9px;margin-bottom:16px}
  .brand-dot{width:30px;height:30px;border-radius:50%;background:var(--green);flex:none}
  .brand-name{font-family:"Montserrat",Arial,sans-serif;font-weight:400;font-size:25px;line-height:1.05;color:var(--navy);letter-spacing:.5px}

  .intro{font-size:8.2px;line-height:1.5;margin-bottom:14px}
  .headline{font-family:"Libre Baskerville",Georgia,serif;font-style:italic;font-weight:700;
    font-size:15px;color:var(--navy);margin-bottom:12px}

  .reasons{list-style:none}
  .reason{display:flex;gap:10px;margin-bottom:10px}
  .reason-num{flex:none;width:19px;height:19px;border-radius:50%;background:var(--green);color:#fff;
    font-size:9px;font-weight:700;display:flex;align-items:center;justify-content:center;margin-top:2px}
  .reason-title{font-size:8.6px;font-weight:700;color:var(--green);margin-bottom:1px}
  .reason-text{font-size:7.8px;line-height:1.45}

  .team-photo{position:absolute;left:72px;bottom:26px;width:250px;height:118px;
    background:linear-gradient(135deg,#c9c4bc 0%,#8f8378 45%,#3c3a3b 100%)}

  .side{position:absolute;left:336px;top:0;width:224px;height:100%}
  .chalkboard-photo{height:248px;background:linear-gradient(160deg,var(--chalk-mid) 0%,var(--chalk-dark) 60%,#6b5e55 100%)}
  .contact-band{height:92px;background:var(--green);color:#fff;padding:22px 14px 0 16px}
  .contact-name{font-size:11px;font-weight:700;margin-bottom:3px}
  .contact-line{font-size:7.4px;line-height:1.45}
  .meeting-photo{height:132px;background:linear-gradient(120deg,#e9e6e2 0%,#b7a796 45%,#4a4f5a 100%)}
</style>
</head>
<body>
  <main class="flyer">
    <div class="accent-tab"></div>

    <section class="main">
      <header class="brand">
        <span class="brand-dot"></span>
        <h1 class="brand-name">Insight Harborworks</h1>
      </header>

      <p class="intro">We are a network of human factors engineers, usability specialists and cognitive scientists who help you design products that people enjoy. Our lab and consulting services cover user research, usability testing, expert reviews and field studies for teams of every size.</p>

      <h2 class="headline">Why Engage Insight Harborworks?</h2>

      <ol class="reasons">
        <li class="reason"><span class="reason-num">1</span><div><h3 class="reason-title">Expertise &amp; Services</h3><p class="reason-text">Our consultants hold advanced degrees in human factors and bring years of practice in research design, usability testing, ethnography and interface evaluation across medical, consumer and software products.</p></div></li>
        <li class="reason"><span class="reason-num">2</span><div><h3 class="reason-title">Range and Dedicated Client Service</h3><p class="reason-text">From a single session to a multi-city study, a dedicated coordinator handles scheduling, hosting and logistics so your team can focus on the findings.</p></div></li>
        <li class="reason"><span class="reason-num">3</span><div><h3 class="reason-title">Onsite and Streaming Videoconferencing</h3><p class="reason-text">Observe sessions from our viewing room or stream them live to your office, with recordings delivered after each day.</p></div></li>
        <li class="reason"><span class="reason-num">4</span><div><h3 class="reason-title">Recruiting</h3><p class="reason-text">A large local database lets us recruit participants by age, occupation, health status and many other criteria.</p></div></li>
        <li class="reason"><span class="reason-num">5</span><div><h3 class="reason-title">Office Space and Accessibility</h3><p class="reason-text">Meeting rooms, private offices and wireless internet near major highways, with ample free parking.</p></div></li>
        <li class="reason"><span class="reason-num">6</span><div><h3 class="reason-title">Transcription and Translation Services</h3><p class="reason-text">Session transcripts and translations in several languages are available on request.</p></div></li>
      </ol>

      <div class="team-photo" role="img" aria-label="Photo of a smiling group of business professionals"></div>
    </section>

    <aside class="side">
      <div class="chalkboard-photo" role="img" aria-label="Photo of a researcher at a chalkboard covered in equations"></div>
      <div class="contact-band">
        <p class="contact-name">Insight Harborworks</p>
        <p class="contact-line">1200 Harbor Lane, Suite 4, Portland, OR 97201</p>
        <p class="contact-line">(503) 555-0142</p>
        <p class="contact-line">www.insightharborworks.com</p>
      </div>
      <div class="meeting-photo" role="img" aria-label="Photo of colleagues reviewing work together at a table"></div>
    </aside>

    <div class="accent-bar"></div>
  </main>
</body>
</html>
```